Professional Services/Construction Management (Millwork) Biz Cards

We've decided on a logo and have our color palette set, now we want to design some very professional looking cards that make a strong first impression - they'll reflect our tagline (that we're going to put on the back: Innovative. Professional. Leaders.

The example business card shows generally the direction we've been thinking of going for the back side - **but we're open to other ideas**

Target Market(s)

The cards should target more high-end (wealthy) owners and general contracting companies. We want them to convey a strong first impression - in a professional and not garish way.

Industry/Entity Type

Construction Company

Contact Information for Business Card

There needs to be a place for our company contractor's license number and business address. We want to also have people's names, titles, phone number, email address. The back can be the logo, tagline and web address

Requirements
Must have
• follow our color palette
Nice to have
• Font & Styles should compliment the Harbor Joinery fonts, but not necessarily match exactly

```html
<!DOCTYPE html>
<html lang="en">
<head>
<meta charset="utf-8">
<title>Harbor Joinery Business Cards</title>
<link href="https://fonts.googleapis.com/css2?family=Noto+Sans:wght@400;500&display=swap" rel="stylesheet">
<style>
  :root {
    --backdrop: #3b3b3b;
    --card-light: #e6e6e6;
    --card-dark: #000000;
    --brand-green: #52903d;
    --brand-brown: #5a4a3f;
    --brand-mauve: #8e7873;
    --seal-grey: #7a7a7a;
    --ink: #111111;
    --rule: #555555;
  }
  * { margin: 0; padding: 0; box-sizing: border-box; }
  html, body { width: 1200px; height: 750px; overflow: hidden; }
  body {
    background: var(--backdrop);
    font-family: "Noto Sans", Tahoma, sans-serif;
    position: relative;
  }
  .card {
    position: absolute;
    top: 215px;
    width: 499px;
    height: 285px;
    overflow: hidden;
  }
  .card--front { left: 88px; background: var(--card-light); }
  .card--back { left: 617px; background: var(--card-dark); }
  .card__band {
    position: absolute; left: 0; right: 0; bottom: 0; height: 25px;
    background: var(--brand-green);
    border-top: 5px solid var(--brand-brown);
  }
  .brand-seal {
    position: absolute;
    border-radius: 50%;
    display: flex; align-items: center; justify-content: center;
    text-align: center;
    font-weight: 500;
  }
  .card--front .brand-seal {
    left: 26px; top: 63px; width: 140px; height: 140px;
    background: var(--brand-mauve);
    border: 6px solid var(--brand-brown);
    color: #ffffff; font-size: 17px; line-height: 1.2;
  }
  .card--back .brand-seal {
    left: 147px; top: 28px; width: 204px; height: 204px;
    background: var(--seal-grey);
    color: var(--ink); font-size: 26px; line-height: 1.15;
  }
  .divider {
    position: absolute; left: 186px; top: 25px; width: 1px; height: 216px;
    background: var(--rule);
  }
  .details { position: absolute; left: 207px; top: 52px; }
  .details__headline {
    color: var(--brand-green); font-size: 27px; font-weight: 400;
    line-height: 1; letter-spacing: -0.2px;
  }
  .details__name { margin-top: 16px; font-size: 21px; color: var(--ink); line-height: 1.1; }
  .details__title { font-size: 15px; color: var(--ink); line-height: 1.2; }
  .contact { list-style: none; margin-top: 14px; }
  .contact li {
    display: flex; align-items: center; gap: 12px;
    font-size: 14px; color: #222; height: 19px;
  }
  .contact svg { width: 10px; height: 10px; flex: none; margin-left: 6px; }
</style>
</head>
<body>
  <section class="card card--front">
    <div class="brand-seal">Harbor<br>Joinery</div>
    <div class="divider"></div>
    <div class="details">
      <h1 class="details__headline">Professional Services</h1>
      <p class="details__name">Daniel Porter</p>
      <p class="details__title">Project Engineer</p>
      <ul class="contact">
        <li>
          <svg viewBox="0 0 10 10" aria-hidden="true"><rect width="10" height="10" rx="1" fill="#52903d"/><path d="M2 4.5c0-1 .8-1.8 3-1.8s3 .8 3 1.8H6.6V3.9H3.4v.6z M3 5h4l.6 2.5H2.4z" fill="#fff"/></svg>
          555 014 2287
        </li>
        <li>
          <svg viewBox="0 0 10 10" aria-hidden="true"><rect width="10" height="10" rx="1" fill="#52903d"/><rect x="2" y="3" width="6" height="4" fill="none" stroke="#fff" stroke-width=".8"/><path d="M2 3l3 2.3L8 3" fill="none" stroke="#fff" stroke-width=".8"/></svg>
          harborjoinery@mail.com
        </li>
        <li>
          <svg viewBox="0 0 10 10" aria-hidden="true"><rect width="10" height="10" rx="1" fill="#52903d"/><path d="M5 8.5C3.5 6.5 3 5.5 3 4.4a2 2 0 0 1 4 0c0 1.1-.5 2.1-2 4.1z" fill="#fff"/><circle cx="5" cy="4.4" r=".7" fill="#52903d"/></svg>
          418 Quarry Ln, Fenton, MO 63026
        </li>
      </ul>
    </div>
    <div class="card__band"></div>
  </section>

  <section class="card card--back">
    <div class="brand-seal">Harbor<br>Joinery</div>
    <div class="card__band"></div>
  </section>
</body>
</html>
```